Business Card

Need a clean, professional, simple, but clever business card for our company LUMO RIDES. We only want to see black and white colors as that reflects the branding of our company. Attaching logo. Will also consider the "sky blue" shown in our web site sample png - but use of the color should be minimal.

Lumo Rides is a executive car service operating in cities throughout Africa. By operating well equipped Varento Halde vehicles, we offer the smoothest and stylish ride in town. We aim to provide customers with a valuable experience. That’s why we make sure our patrons get picked up like a boss, travel in style, and Ride in Style.

We need a card that says that. Likely to print on the best quality/smoothest paper available, as it must speak volumes of our business and class.

We would like the rear of the card to be all black. Perhaps we can put the web url on it, or leave it blank if it looks neater/more elegant.

Use the following contact information (as you see fit):

Lumo Rides Limited
P.O. Box 58104
Dar es Salaam, Tanzania

Baraka Kilonzo
Managing Director

+255 (0) 712 904618
sales@lumorides.example

web url: www.lumorides.example
email: chauffeur@lumorides.example

***Winning designer will likely be commissioned for more promotional work in near future.

Target Market(s)

The target market for this card is corporate executives of top firms (financial, consulting, businessmen, etc). They are interested in high quality transportation. Our fleet is all high end Varento Halde black cars (black exterior, black interior); and therefore, that high end quality and promptness must be reflected in the card. Also simplicity, as we we take care of all the little details behind the scene.

Industry/Entity Type

Business

Requirements
Must have
• Font must be: Helvetica Neue, like the logo. You may use other variations (Thin, Ultra thin, Regular, Bold), so long as it looks and prints well.

If web url is included on the back of the card, then do NOT include it also on the front.
Nice to have
• If there is something nice and clever that you can do/think of that doesn't make the card look busy, but adds a little "posh", then I could be even more interested.

However, if there's no little thing do be done, I'd rather a simple, but very professional looking card that attracts a lot of attention.

```html
<!DOCTYPE html>
<html lang="en">
<head>
<meta charset="utf-8">
<title>Lumo Rides — Business Card</title>
<link rel="stylesheet" href="https://fonts.googleapis.com/css2?family=Inter:wght@200;300;400;700&display=swap">
<style>
  :root {
    --backdrop: #463e39;
    --card-black: #0e0e0f;
    --card-edge: #1c1c1e;
    --emboss: #1d1d1f;
    --emboss-light: #262628;
    --white: #f4f4f4;
    --soft-white: #d9d9d9;
    --sky-blue: #1fa3c9;
  }
  * { margin: 0; padding: 0; box-sizing: border-box; }
  html, body {
    width: 1200px;
    height: 716px;
    overflow: hidden;
  }
  body {
    background: var(--backdrop);
    font-family: "Inter", "Helvetica Neue", Helvetica, Arial, sans-serif;
    position: relative;
  }
  .card {
    position: absolute;
    top: 206px;
    width: 525px;
    height: 300px;
    background: var(--card-black);
    border: 1px solid var(--card-edge);
    border-radius: 3px;
    box-shadow: 0 18px 40px rgba(0, 0, 0, 0.45);
    overflow: hidden;
  }
  .card--back { left: 50px; }
  .card--front { left: 625px; }

  /* Back */
  .back-wordmark {
    position: absolute;
    left: 34px;
    top: 92px;
    font-size: 64px;
    font-weight: 300;
    letter-spacing: 2px;
    color: var(--emboss);
    text-shadow: 0 1px 0 var(--emboss-light);
    white-space: nowrap;
  }
  .back-tagline {
    position: absolute;
    left: 36px;
    top: 168px;
    font-size: 15px;
    font-weight: 300;
    color: var(--sky-blue);
  }

  /* Front */
  .wordmark {
    position: absolute;
    left: 34px;
    top: 58px;
    font-size: 40px;
    font-weight: 300;
    letter-spacing: 1.5px;
    color: var(--white);
    white-space: nowrap;
  }
  .holder {
    position: absolute;
    left: 320px;
    top: 120px;
    color: var(--white);
  }
  .holder__name {
    font-size: 17px;
    font-weight: 700;
  }
  .holder__role {
    margin-top: 2px;
    font-size: 11px;
    font-weight: 400;
    letter-spacing: 0.4px;
    color: var(--soft-white);
  }
  .website {
    position: absolute;
    left: 34px;
    top: 178px;
    font-size: 13px;
    font-weight: 400;
    letter-spacing: 1.5px;
    color: var(--sky-blue);
  }
  .contact {
    position: absolute;
    right: 34px;
    bottom: 34px;
    text-align: right;
    font-size: 13px;
    font-weight: 300;
    line-height: 1.45;
    color: var(--white);
  }
</style>
</head>
<body>
  <section class="card card--back" aria-label="Card back">
    <div class="back-wordmark">LUMO RIDES</div>
    <div class="back-tagline">Ride in Style.</div>
  </section>

  <section class="card card--front" aria-label="Card front">
    <div class="wordmark">LUMO RIDES</div>
    <div class="holder">
      <div class="holder__name">Baraka Kilonzo</div>
      <div class="holder__role">MANAGING DIRECTOR</div>
    </div>
    <div class="website">www.lumorides.example</div>
    <div class="contact">
      <div class="contact__phone">+255 (0) 712 904618</div>
      <div class="contact__email">chauffeur@lumorides.example</div>
    </div>
  </section>
</body>
</html>
```